"Breakthrough! Mapping the Coastal Escape" NEEDS BOOK COVER!

Hello - please see the attached BOOK COVER DESIGN BRIEF document for full instructions and content required for cover.

I am really seeking clean, professional designs here that follow my instructions. The cover MUST jump out in a thumbnail (as if on Brindlow) - any covers that are too busy, messy or unprofessional will be eliminated.

Any questions please ask.

Thanks.
Colin
Updates

Project Deadline Extended
Reason: This project has been extended to invite more designers, as I haven't received enough options to choose from. Hoping this extra few days allows a few more submissions. Thank you to existing designers for your submissions, a number of them are in the running.

Target Market(s)

Please see the attached brief for full instructions on this project.

Industry/Entity Type

Property

Font styles to use
Serif
Sans Serif

Requirements
Must have
• Please see the attached brief for full instructions on this project.
Nice to have
Should not have

```html
<!DOCTYPE html>
<html lang="en">
<head>
<meta charset="utf-8">
<title>Breakthrough! Mapping the Coastal Escape — Book Cover</title>
<link href="https://fonts.googleapis.com/css2?family=Open+Sans:ital,wght@0,300;0,400;0,600;0,700;0,800;1,400;1,700&display=swap" rel="stylesheet">
<style>
:root{
  --navy:#0d2a66;
  --blue:#0c55a5;
  --stage:#e8e9eb;
  --paper:#ffffff;
  --white:#ffffff;
}
*{margin:0;padding:0;box-sizing:border-box}
html,body{width:1200px;height:857px;overflow:hidden;background:var(--stage)}
body{font-family:"Open Sans",Arial,sans-serif;color:var(--navy);position:relative}
.spread{position:absolute;left:50px;top:50px;width:1100px;height:758px;background:var(--paper);box-shadow:0 2px 10px rgba(0,0,0,.25)}
.abs{position:absolute}
.ln{display:block;white-space:nowrap}
.j{text-align:justify;text-align-last:justify}

/* back cover */
.back-authors{right:575px;top:21px;font-weight:700;font-size:14px;line-height:18px;white-space:nowrap}
.back-title{left:12px;top:44px;font-weight:800;font-size:21px;line-height:28px;white-space:nowrap;letter-spacing:-.2px}
.back-title .lead{color:var(--blue)}
.back-sub{left:12px;top:74px;font-weight:700;font-size:13px;line-height:16px;white-space:nowrap;letter-spacing:-.1px}
.back-copy{font-size:11.8px;line-height:15px;letter-spacing:-.15px}
.back-intro{left:12px;top:89px;width:513px}
.back-list{left:12px;top:125px;width:521px;list-style:none}
.back-list li{padding-left:12px;position:relative}
.back-list li::before{content:"•";position:absolute;left:0}
.back-pitch{left:12px;top:272px;width:513px;line-height:14.6px}
.testimonials{left:0;top:350px;width:535px;height:108px;background:var(--blue);color:var(--white);display:flex;gap:16px;padding:4px 10px 0 12px}
.testimonial{flex:1;font-size:9.9px;line-height:13.4px}
.testimonial cite{display:block;text-align:right;font-weight:700;font-style:italic}
.portrait{background:linear-gradient(160deg,#d9c3a6,#b98e70 60%,#e8e1d8);border:1px solid var(--navy)}
.portrait-helena{left:12px;top:467px;width:91px;height:91px}
.portrait-graham{left:432px;top:566px;width:91px;height:92px}
.bio{font-size:10.3px;line-height:14px}
.bio b{font-style:italic}
.bio-helena{left:110px;top:470px;width:415px}
.bio-graham{left:12px;top:570px;width:414px}
.publisher{left:34px;top:674px;width:196px;text-align:center}
.publisher-mark{margin:0 auto;width:116px;height:41px;display:flex;align-items:center;justify-content:center;gap:6px;background:var(--navy);color:var(--white);font-weight:700;font-size:14px}
.publisher-mark i{width:8px;height:8px;background:var(--white);display:block}
.publisher-name{font-size:11.5px;line-height:16px;margin-top:3px;white-space:nowrap}
.publisher-web{font-size:6.5px;font-weight:600;white-space:nowrap}

/* spine */
.spine-text{writing-mode:vertical-rl;font-weight:700;white-space:nowrap;left:540px;line-height:16px}
.spine-authors{top:42px;font-size:11.5px;color:var(--blue)}
.spine-title{top:282px;font-size:12px;font-weight:800}
.spine-mark{left:540px;top:640px;width:16px;height:46px;background:var(--navy);color:var(--white);writing-mode:vertical-rl;font-size:7.5px;font-weight:700;display:flex;align-items:center;justify-content:center}

/* front cover */
.stamp{left:577px;top:15px;width:288px;height:145px;border:7px solid var(--blue);transform:rotate(-6deg);display:flex;align-items:center;justify-content:center}
.stamp span{font-weight:800;font-size:29px;color:var(--blue);letter-spacing:-.3px;white-space:nowrap}
.front-authors{right:52px;top:155px;font-weight:700;font-size:16px;line-height:20px;color:var(--blue);white-space:nowrap}
.front-main{left:616px;top:168px;font-weight:300;font-size:98px;line-height:100px;letter-spacing:1px;white-space:nowrap}
.front-the{left:994px;top:248px;font-weight:800;font-size:22px;line-height:26px}
.front-bold{left:616px;top:274px;font-weight:800;font-size:45px;line-height:52px;white-space:nowrap}
.front-band{left:565px;top:331px;width:535px;height:86px;background:var(--blue);color:var(--white);text-align:center;font-size:19.5px;line-height:24.5px;padding-top:6px}
.front-band b{font-weight:700}
.front-photo{left:565px;top:428px;width:510px;height:330px;background:radial-gradient(ellipse at 45% 55%,#e4c3a8 0%,#d7b497 20%,#dde4ef 45%,#fff 72%)}
.arrow{left:0;top:252px}
</style>
</head>
<body>
<div class="spread">

  <!-- back cover -->
  <div class="abs back-authors">Graham Whitford &amp; Helena Markovic</div>
  <div class="abs back-title"><span class="lead">BREAKTHROUGH!</span> MAPPING THE COASTAL ESCAPE</div>
  <div class="abs back-sub">Everything You Didn’t Know About Property And Mortgages, But Wish You Did!</div>
  <p class="abs back-copy back-intro">
    <span class="ln j">Breakthrough! Mapping the Coastal Escape is the smart home buyers guide to mortgages,</span>
    <span class="ln">property, investing and making your dreams reality. This easy to read book will teach you:</span>
  </p>
  <ul class="abs back-copy back-list">
    <li><span class="ln">Five things you must know before buying a property and mortgage – don’t approach any</span><span class="ln">bank or broker before understanding this.</span></li>
    <li><span class="ln">How to maximise your chances of getting your loan approved – including help on deposit</span><span class="ln">savings and working out how much you can borrow.</span></li>
    <li><span class="ln">The mortgage and property process explained in six easy steps – with the five stressful</span><span class="ln">mortgage mistakes to avoid.</span></li>
    <li><span class="ln">Tips to getting smarter with your money and how to pay off your home loan in record time.</span></li>
    <li><span class="ln">The accidental investor vs. the planned investor – and why most Australians invest for the</span></li>
  </ul>

  <svg class="abs arrow" width="1000" height="16" viewBox="0 0 1000 16" aria-hidden="true">
    <rect x="0" y="6" width="966" height="4" fill="#0c55a5"/>
    <polygon points="962,0 988,8 962,16" fill="#0c55a5"/>
  </svg>

  <div class="abs back-copy back-pitch">
    <span class="ln j">The Great Australian Dream of owning your own property, or starting an investment</span>
    <span class="ln j">portfolio, can become a great Australian nightmare if you don’t have the right knowledge and</span>
    <span class="ln">team to support you and your dreams.</span>
    <span class="ln j">So before taking your next step, read this book carefully and get the insider tips to make</span>
    <span class="ln">confident decisions with your money and your future.</span>
  </div>

  <div class="abs testimonials">
    <blockquote class="testimonial">
      <span class="ln j">“I was reluctant in the past to deal with a broker</span>
      <span class="ln j">rather than a major bank. Graham has changed this.</span>
      <span class="ln j">He is a totally professional, knowledgeable man –</span>
      <span class="ln j">who is genuinely happy to deal with us. He worked</span>
      <span class="ln j">hard to make us happy with the best deal possible.</span>
      <span class="ln j">His help has turned us from having nothing to</span>
      <span class="ln">being totally financially independent.”</span>
      <cite>- Peter Lanham, Cairns, QLD</cite>
    </blockquote>
    <blockquote class="testimonial">
      <span class="ln j">“Graham professionally guided me through the</span>
      <span class="ln j">process of applying for my first home loan. He</span>
      <span class="ln j">made what would normally be a worrying task</span>
      <span class="ln j">into something enjoyable and stress-free. I found</span>
      <span class="ln j">Graham’s knowledge and confidence in the home</span>
      <span class="ln j">loan market impressive. Thank you for helping me</span>
      <span class="ln">make my first big step into a positive future.”</span>
      <cite>- Mark Ellison, QLD</cite>
    </blockquote>
  </div>

  <div class="abs portrait portrait-helena" role="img" aria-label="Author portrait of Helena Markovic"></div>
  <p class="abs bio bio-helena">
    <span class="ln j"><b>Helena Markovic</b> bought her first investment property in 1995 and has never</span>
    <span class="ln j">looked back. As Managing Director of Harbourline Finance Cairns, she ensures all</span>
    <span class="ln j">clients receive the highest level of personal service every step of the way, and</span>
    <span class="ln j">enjoys helping people achieve their dream of getting into their own home or</span>
    <span class="ln j">start investing. With three generations of one family as clients, Helena is</span>
    <span class="ln j">driven to share her experiences in property and mortgages – so you too can learn</span>
    <span class="ln">the easy way and avoid costly mistakes with your money.</span>
  </p>

  <p class="abs bio bio-graham">
    <span class="ln j"><b>Graham Whitford</b> is an award winning mortgage broker with Harbourline Finance</span>
    <span class="ln j">Cairns. With over 40 years’ experience in the finance world, he’s worked in</span>
    <span class="ln j">virtually every area of banking and lending in over a dozen different locations</span>
    <span class="ln j">throughout Queensland. Along the way he’s helped thousands of Australians secure</span>
    <span class="ln j">finance for their dream home or investment property. No matter how simple or</span>
    <span class="ln j">complex the challenge, with a world of insider knowledge and experience at his</span>
    <span class="ln">fingertips, you definitely want Graham to be on your finance team.</span>
  </p>
  <div class="abs portrait portrait-graham" role="img" aria-label="Author portrait of Graham Whitford"></div>

  <div class="abs publisher">
    <div class="publisher-mark"><i></i>Harbourline</div>
    <div class="publisher-name">Harbourline Finance Cairns</div>
    <div class="publisher-web">WWW.HARBOURLINEFINANCE.COM.AU</div>
  </div>

  <!-- spine -->
  <div class="abs spine-text spine-authors">Graham Whitford &amp; Helena Markovic</div>
  <div class="abs spine-text spine-title">BREAKTHROUGH! MAPPING THE COASTAL ESCAPE</div>
  <div class="abs spine-mark">Harbourline</div>

  <!-- front cover -->
  <div class="abs stamp"><span>BREAKTHROUGH</span></div>
  <div class="abs front-authors">Graham Whitford &amp; Helena Markovic</div>
  <div class="abs front-main">MAPPING</div>
  <div class="abs front-the">THE</div>
  <div class="abs front-bold">COASTAL ESCAPE</div>
  <div class="abs front-band">The Smart Home Buyers <b>Guide To</b><br><b>Mortgages, Property, Investing</b> and<br><b>Making Your Dreams Reality!</b></div>
  <div class="abs front-photo" role="img" aria-label="Photo of a hand in a blue shirt sleeve holding out house keys on a house-shaped key ring"></div>

</div>
</body>
</html>
```